Labour Day banner showcasing 20% off site

Banner graphic promoting our Labour Day sale
Size: 2000px x 600px
- examples from other companies and their sale banners have been uploaded for inspiration. Labour day examples are for the United States's holiday and submissions should NOT be in their country colours.
- product images can be found at www.tallpinegreens.com

Target Market(s)

19+

Industry/Entity Type

Cannabis

Requirements
Must have
• Phrases:
- “Happy Labour Day”
- “20% off site wide sale*"
- "Coupon code: Harvest20"
- Underneath phrase the date of sale “September 3rd - 7th”
- In tiny print “*excludes all sale and bundled items”
- MUST BE 2000px x 600px
Nice to have
• - images of the products or bud we carry which can be found at www.tallpinegreens.com
- bold
Should not have
• - company logo
- the American flag, we are a Canadian company, colours and flag should all be Canadian

```html
<!DOCTYPE html>
<html lang="en">
<head>
<meta charset="utf-8">
<title>Happy Labour Day Sale Banner</title>
<link rel="stylesheet" href="https://fonts.googleapis.com/css2?family=Poppins:wght@500;600;800;900&display=swap">
<style>
  :root {
    --stage: #5f5f5f;
    --banner-dark: #1d1d1d;
    --banner-mid: #262626;
    --leaf-green: #7dc242;
    --white: #ffffff;
    --tile-black: #141414;
  }
  * { margin: 0; padding: 0; box-sizing: border-box; }
  html, body {
    width: 1200px;
    height: 480px;
    overflow: hidden;
    background: var(--stage);
    font-family: "Poppins", sans-serif;
  }
  .sale-banner {
    position: absolute;
    left: 0;
    top: 60px;
    width: 1200px;
    height: 360px;
    background: radial-gradient(ellipse at 65% 45%, var(--banner-mid), var(--banner-dark) 75%);
    overflow: hidden;
  }
  .product-mosaic {
    position: absolute;
    left: 0;
    top: 0;
    width: 440px;
    height: 360px;
  }
  .headline {
    position: absolute;
    left: 400px;
    width: 730px;
    top: 8px;
    text-align: center;
    color: var(--leaf-green);
    font-weight: 800;
    font-size: 70px;
    line-height: 84px;
    letter-spacing: 0.5px;
  }
  .offer-frame {
    position: absolute;
    left: 398px;
    top: 104px;
    width: 727px;
    height: 173px;
    border: 1.5px solid var(--leaf-green);
  }
  .offer-dates,
  .offer-scope {
    position: absolute;
    left: 50%;
    transform: translate(-50%, -50%);
    background: var(--banner-dark);
    color: var(--white);
    font-weight: 600;
    font-size: 17px;
    letter-spacing: 3.5px;
    padding: 0 14px;
    white-space: nowrap;
  }
  .offer-dates { top: -1px; }
  .offer-scope { top: 100%; }
  .offer-discount {
    position: absolute;
    left: 0;
    right: 0;
    top: 14px;
    text-align: center;
    color: var(--white);
    font-weight: 800;
    font-size: 106px;
    line-height: 120px;
    letter-spacing: 1px;
  }
  .offer-coupon {
    position: absolute;
    left: 0;
    right: 0;
    top: 125px;
    text-align: center;
    color: var(--leaf-green);
    font-weight: 500;
    font-size: 25px;
    letter-spacing: 3.5px;
  }
  .offer-coupon strong { font-weight: 600; }
  .fine-print {
    position: absolute;
    left: 400px;
    width: 727px;
    top: 298px;
    text-align: center;
    color: var(--leaf-green);
    font-weight: 500;
    font-size: 15px;
  }
</style>
</head>
<body>
  <section class="sale-banner">
    <svg class="product-mosaic" viewBox="0 0 440 360" xmlns="http://www.w3.org/2000/svg">
      <defs>
        <linearGradient id="bud-tones" x1="0" y1="0" x2="1" y2="1">
          <stop offset="0" stop-color="#8d9468"/>
          <stop offset="1" stop-color="#5d6240"/>
        </linearGradient>
        <linearGradient id="gold-bud-tones" x1="0" y1="0" x2="1" y2="1">
          <stop offset="0" stop-color="#b79a6a"/>
          <stop offset="1" stop-color="#7f6a44"/>
        </linearGradient>
        <linearGradient id="tincture-tones" x1="0" y1="0" x2="1" y2="1">
          <stop offset="0" stop-color="#2f5b63"/>
          <stop offset="1" stop-color="#e9eeee"/>
        </linearGradient>
        <linearGradient id="edible-tones" x1="0" y1="0" x2="1" y2="1">
          <stop offset="0" stop-color="#d8c3a5"/>
          <stop offset="1" stop-color="#8cc79a"/>
        </linearGradient>
      </defs>

      <polygon class="accent-green" points="0,40 0,360 245,360 410,195 330,115" fill="var(--leaf-green)"/>
      <polygon class="accent-white" points="275,0 400,0 338,72" fill="var(--white)"/>
      <polygon class="accent-white" points="248,360 372,360 310,296" fill="var(--white)"/>

      <g class="product-tile" transform="translate(165 75) rotate(45)">
        <rect x="-62" y="-62" width="124" height="124" fill="var(--tile-black)"/>
        <rect x="-54" y="-54" width="108" height="108" fill="var(--leaf-green)"/>
        <rect x="-46" y="-46" width="92" height="92" fill="var(--white)"/>
        <g role="img" aria-label="Cannabis flower bud">
          <rect x="-30" y="-30" width="60" height="60" rx="24" fill="url(#bud-tones)"/>
        </g>
      </g>
      <g class="product-tile" transform="translate(77 163) rotate(45)">
        <rect x="-62" y="-62" width="124" height="124" fill="var(--tile-black)"/>
        <rect x="-54" y="-54" width="108" height="108" fill="var(--leaf-green)"/>
        <rect x="-46" y="-46" width="92" height="92" fill="var(--white)"/>
        <g role="img" aria-label="Tin of edible gummies">
          <rect x="-32" y="-32" width="64" height="64" rx="8" fill="url(#edible-tones)"/>
        </g>
      </g>
      <g class="product-tile" transform="translate(253 163) rotate(45)">
        <rect x="-62" y="-62" width="124" height="124" fill="var(--tile-black)"/>
        <rect x="-54" y="-54" width="108" height="108" fill="var(--leaf-green)"/>
        <rect x="-46" y="-46" width="92" height="92" fill="var(--white)"/>
        <g role="img" aria-label="CBD oil tincture bottle with box">
          <rect x="-30" y="-30" width="60" height="60" rx="6" fill="url(#tincture-tones)"/>
        </g>
      </g>
      <g class="product-tile" transform="translate(165 251) rotate(45)">
        <rect x="-62" y="-62" width="124" height="124" fill="var(--tile-black)"/>
        <rect x="-54" y="-54" width="108" height="108" fill="var(--leaf-green)"/>
        <rect x="-46" y="-46" width="92" height="92" fill="var(--white)"/>
        <g role="img" aria-label="Cannabis flower bud">
          <rect x="-30" y="-30" width="60" height="60" rx="24" fill="url(#gold-bud-tones)"/>
        </g>
      </g>
    </svg>

    <h1 class="headline">HAPPY LABOUR DAY</h1>

    <div class="offer-frame">
      <p class="offer-dates">SEPTEMBER 3RD - 7TH</p>
      <p class="offer-discount">20% OFF</p>
      <p class="offer-coupon">COUPON CODE: <strong>HARVEST20</strong></p>
      <p class="offer-scope">SITE WIDE SALE</p>
    </div>

    <p class="fine-print">excludes all sale and bundled items</p>
  </section>
</body>
</html>
```